Einladungskarten für Firmenjubiläum
Zielgruppe
Ich brauche eine digitale Einladungskarte zum 10-jährigen Firmenjubiläum, das am 12. Juli stattfinden soll. Zu uns; wir sind ein Ingenieurbüro im Bereich Digitalisierung und sicherheitskritische Systeme, wie sie in Flugzeugen, medizinischen Geräten, modernen Autos etc. vorkommen. Autonomes Fahren und Raumfahrtmedizin, sowie Fahrzeugsicherheit und Cyber-Sicherheit gehören z. B. zu unseren Schwerpunktthemen.
Aufgabenstellung
Ich bin für Ideen offen, die sich an dem Inhalt unserer Website anlehnen.

```html
<!DOCTYPE html>
<html lang="de">
<head>
<meta charset="utf-8">
<title>Einladung – 10-jähriges Firmenjubiläum</title>
<link rel="stylesheet" href="https://fonts.googleapis.com/css2?family=Roboto:wght@300;400;700&display=swap">
<style>
  :root {
    --bg: #000000;
    --neon-text: #a9d4ff;
    --neon-glow: #2f7dff;
    --neon-core: #d6ecff;
    --neon-edge: #1f63ff;
  }
  html, body {
    margin: 0;
    padding: 0;
    width: 1200px;
    height: 1200px;
    overflow: hidden;
    background: var(--bg);
  }
  .invitation {
    position: relative;
    width: 1200px;
    height: 1200px;
    background: var(--bg);
    font-family: "Roboto", Arial, sans-serif;
    color: var(--neon-text);
  }
  .neon-text {
    text-shadow:
      0 0 4px var(--neon-glow),
      0 0 12px var(--neon-glow),
      0 0 24px rgba(47, 125, 255, 0.6);
  }
  .invitation__intro {
    position: absolute;
    top: 142px;
    left: 0;
    width: 100%;
    margin: 0;
    text-align: center;
    font-weight: 300;
    font-size: 47px;
    line-height: 60px;
    letter-spacing: 0.5px;
  }
  .invitation__number {
    position: absolute;
    inset: 0;
    width: 1200px;
    height: 1200px;
  }
  .invitation__number text {
    font-family: "Roboto", Arial, sans-serif;
    font-weight: 700;
    font-size: 570px;
    letter-spacing: -20px;
    fill: none;
  }
  .number-glow {
    stroke: var(--neon-edge);
    stroke-width: 10;
  }
  .number-core {
    stroke: var(--neon-core);
    stroke-width: 3;
  }
  .invitation__occasion {
    position: absolute;
    top: 880px;
    left: 246px;
    margin: 0;
    font-weight: 300;
    font-size: 50px;
    letter-spacing: 0.5px;
  }
  .invitation__details {
    position: absolute;
    top: 1106px;
    left: 0;
    width: 100%;
    margin: 0;
    text-align: center;
    font-weight: 400;
    font-size: 35px;
    white-space: pre;
  }
</style>
</head>
<body>
  <main class="invitation">
    <p class="invitation__intro neon-text">Sie sind herzlich eingeladen<br>zu unserem</p>

    <svg class="invitation__number" viewBox="0 0 1200 1200" aria-label="10">
      <defs>
        <filter id="neon-glow" x="-20%" y="-20%" width="140%" height="140%">
          <feGaussianBlur stdDeviation="10" result="blur"/>
          <feMerge>
            <feMergeNode in="blur"/>
            <feMergeNode in="blur"/>
            <feMergeNode in="SourceGraphic"/>
          </feMerge>
        </filter>
      </defs>
      <text class="number-glow" x="600" y="756" text-anchor="middle" filter="url(#neon-glow)">10</text>
      <text class="number-core" x="600" y="756" text-anchor="middle">10</text>
    </svg>

    <p class="invitation__occasion neon-text">-jährigen Firmenjubiläum</p>

    <p class="invitation__details neon-text">12. Juli / 20 Uhr - Birkenhainer Weg 8  - 21670 Elmsdorf</p>
  </main>
</body>
</html>
```